Letterhead for small civil engineer company

We need bold and modern design for company letterhead in MS word. It needs to have company logo and company info. Somewhere in the upper right part of document needs to be space for "recever" and the documents starts with, example, "SUBJECT: CIVIL ENGINEER LETTERHEAD".

in the bottom part of document needs to be signature and date.

Company info: Veltrana d.o.o., Lipovac 15, Lipovac (Općina Brdarić), OIB 47396028154, www.veltrana.hr, info@veltrana.hr

Email of document sender needs to be somewhere if document, exapmle xyz@veltrana.hr

Target Market(s)

Civil engineer company and projects

Industry/Entity Type

Civil engineer

Font styles to use
Serif

Colors
F0912C
F2A743
F7CA91
FBE8D2
FDF5EE

Requirements
Must have
• Company logo and company info
Nice to have
• Moder and clean design
Should not have
• Too much details

```html
<!DOCTYPE html>
<html lang="hr">
<head>
<meta charset="utf-8">
<title>Veltrana d.o.o. – Letterhead</title>
<link rel="stylesheet" href="https://fonts.googleapis.com/css2?family=Tinos:wght@400;700&family=Parisienne&display=swap">
<style>
  :root {
    --paper: #ffffff;
    --ink: #333333;
    --brand-orange: #f0912c;
    --orange-mid: #f2a743;
    --orange-soft: #f7ca91;
    --orange-pale: #fbe8d2;
    --orange-whisper: #fdf5ee;
    --charcoal: #2f2d30;
  }
  * { box-sizing: border-box; margin: 0; padding: 0; }
  html, body { width: 848px; height: 1200px; overflow: hidden; background: var(--paper); }
  .letterhead {
    position: relative;
    width: 848px;
    height: 1200px;
    background: var(--paper);
    font-family: "Tinos", "Times New Roman", serif;
    color: var(--ink);
    overflow: hidden;
  }
  .building-backdrop {
    position: absolute;
    left: 0; top: 456px;
    width: 848px; height: 660px;
  }
  .brand {
    position: absolute;
    left: 107px; top: 122px;
    display: flex; align-items: center; gap: 12px;
  }
  .brand-square {
    width: 30px; height: 30px;
    border: 2px solid var(--brand-orange);
  }
  .brand-name {
    font-size: 34px;
    font-weight: 400;
    letter-spacing: 2px;
    color: var(--brand-orange);
    line-height: 1;
  }
  .sender {
    position: absolute;
    left: 606px; top: 128px;
    display: flex; align-items: center; gap: 12px;
    font-size: 14px;
  }
  .sender-mark {
    width: 25px; height: 25px;
    background: var(--brand-orange);
    border-radius: 3px;
  }
  .receiver {
    position: absolute;
    left: 577px; top: 214px;
    font-size: 14px;
  }
  .subject {
    position: absolute;
    left: 107px; top: 366px;
    font-size: 15px;
    font-weight: 700;
    text-transform: uppercase;
  }
  .signature-name {
    position: absolute;
    left: 108px; top: 838px;
    font-family: "Parisienne", cursive;
    font-size: 34px;
    color: #222;
  }
  .sign-label, .date-label {
    position: absolute;
    top: 896px;
    font-size: 14px;
  }
  .sign-label { left: 108px; }
  .date-label { left: 579px; }
  .company-info {
    position: absolute;
    left: 107px; top: 1048px;
    font-size: 13.5px;
    line-height: 1.25;
  }
  .footer-band {
    position: absolute;
    left: 0; bottom: 0;
    width: 848px; height: 90px;
  }
</style>
</head>
<body>
<main class="letterhead">
  <svg class="building-backdrop" viewBox="0 0 848 660" role="img" aria-label="Faint line illustration of a modern building">
    <defs>
      <linearGradient id="backdropTone" x1="0" y1="0" x2="1" y2="1">
        <stop offset="0" stop-color="#ffffff" stop-opacity="0"/>
        <stop offset="0.5" stop-color="#f3f3f3" stop-opacity="0.7"/>
        <stop offset="1" stop-color="#ececec" stop-opacity="0.9"/>
      </linearGradient>
    </defs>
    <rect width="848" height="660" fill="url(#backdropTone)"/>
  </svg>

  <header>
    <div class="brand">
      <span class="brand-square"></span>
      <span class="brand-name">VELTRANA</span>
    </div>
    <div class="sender">
      <span class="sender-email">xyz@veltrana.hr</span>
      <span class="sender-mark"></span>
    </div>
  </header>

  <p class="receiver">Recever</p>
  <h1 class="subject">Subject: Civil engineer letterhead</h1>

  <p class="signature-name">Ivan Marek</p>
  <p class="sign-label">Signature</p>
  <p class="date-label">Date,</p>

  <footer class="company-info">
    Company info: Veltrana d.o.o., Lipovac 15, Lipovac (Općina Brdarić), OIB 47396028154,<br>
    www.veltrana.hr, info@veltrana.hr
  </footer>

  <svg class="footer-band" viewBox="0 0 848 90" preserveAspectRatio="none" aria-hidden="true">
    <rect x="330" y="30" width="518" height="60" fill="var(--orange-whisper)"/>
    <rect x="330" y="30" width="518" height="60" fill="var(--orange-pale)" opacity="0.6"/>
    <path d="M160 0 C250 0 300 30 330 90 L240 90 C220 40 200 10 160 0 Z" fill="var(--orange-soft)"/>
    <path d="M190 0 C270 0 330 30 370 90 L300 90 C270 40 240 8 190 0 Z" fill="var(--brand-orange)"/>
    <path d="M0 0 L180 0 C250 5 290 40 320 90 L0 90 Z" fill="var(--charcoal)"/>
  </svg>
</main>
</body>
</html>
```